Etikettendesign für Imkereiprodukt
Zielgruppe
Ich betreibe eine Imkerei nach ökologischen Gesichtspunkten und vertreibe alles rund um die Biene- Honig, Wachs, Met, Likör...
Aus Bienenwachs und reinem Leinöl stelle ich ein natürliches Holzwachs her. (Wachs stammt aus eigener Bio Imkerei, Leinöl wird in Deutschland hergestellt)
Mit dem Wachs werden unbehandelte Hölzer imprägniert, gegen Feuchtigkeit geschützt, das Wachs verleiht dem Holz einen matten Glanz
Für dieses Produkt benötige ich ein Etikett.
Aufgabenstellung
- rundes Etikett Durchmesser 85 mm
- Verwendung von eigenem Firmenlogo (Anhang) (Name der Imkerei auch 'Wabenritter')
- Verwendung von folgenden Textbausteinen:
'ausschließlich Leinöl und Bienenwachs'
'regional von Hand hergestellt'
'komplett ohne Lösungsmittel'
oder ähnlich
- Herstelleradresse
- Datei nach Druck-vorgaben

```html
<!DOCTYPE html>
<html lang="de">
<head>
<meta charset="utf-8">
<title>Wabenritter Holzwachs – Etikett</title>
<link rel="stylesheet" href="https://fonts.googleapis.com/css2?family=Uncial+Antiqua&family=Cabin:wght@400&family=Roboto+Condensed:wght@400;700&display=swap">
<style>
  :root {
    --backdrop: #e9e8ea;
    --ring-light: #cfcba2;
    --ring-dark: #969264;
    --olive: #767341;
    --cream-top: #e9dbbd;
    --cream-mid: #f6f0e4;
    --cream-low: #efe5d2;
    --gold: #b99658;
    --brown: #452a17;
    --white: #ffffff;
  }
  * { margin: 0; padding: 0; box-sizing: border-box; }
  html, body {
    width: 1200px; height: 948px; overflow: hidden;
    background: var(--backdrop);
  }
  .label {
    position: relative;
    width: 1200px; height: 948px;
  }
  .label__shape {
    position: absolute; left: 0; top: 0;
  }
  .label__text {
    position: absolute; left: 0; width: 1200px;
    text-align: center; white-space: nowrap;
  }
  .brand-name {
    top: 380px;
    font-family: "Uncial Antiqua", serif;
    font-size: 31px; letter-spacing: 2px;
    color: var(--gold);
  }
  .product-title {
    top: 418px;
    font-family: "Uncial Antiqua", serif;
    font-size: 92px; line-height: 1; letter-spacing: 3px;
    color: var(--gold);
    text-shadow: 3px 3px 0 var(--brown);
  }
  .product-claim {
    top: 532px;
    font-family: "Cabin", sans-serif;
    font-size: 19px; line-height: 25px;
    color: var(--brown);
  }
  .net-weight {
    top: 600px;
    font-family: "Uncial Antiqua", serif;
    font-size: 30px; letter-spacing: 3px;
    color: var(--brown);
  }
  .producer {
    top: 674px;
    font-family: "Roboto Condensed", sans-serif;
    font-size: 18px; line-height: 21.5px;
    color: var(--white);
  }
  .producer__name { font-weight: 700; }
</style>
</head>
<body>
<main class="label">
  <svg class="label__shape" width="1200" height="948" viewBox="0 0 1200 948" aria-hidden="true">
    <defs>
      <linearGradient id="ring-fill" x1="0" y1="0" x2="1" y2="1">
        <stop offset="0" stop-color="var(--ring-dark)"/>
        <stop offset="0.5" stop-color="var(--ring-light)"/>
        <stop offset="1" stop-color="var(--ring-dark)"/>
      </linearGradient>
      <linearGradient id="face-fill" x1="0" y1="0" x2="0" y2="1">
        <stop offset="0" stop-color="var(--cream-top)"/>
        <stop offset="0.45" stop-color="var(--cream-mid)"/>
        <stop offset="1" stop-color="var(--cream-low)"/>
      </linearGradient>
      <clipPath id="face-clip"><circle cx="600" cy="474" r="341"/></clipPath>
    </defs>
    <circle class="outer-ring" cx="600" cy="474" r="372" fill="url(#ring-fill)"/>
    <circle class="olive-ring" cx="600" cy="474" r="350" fill="var(--olive)"/>
    <circle class="label-face" cx="600" cy="474" r="344" fill="url(#face-fill)"/>
    <rect class="address-band" x="200" y="654" width="800" height="200" fill="var(--brown)" clip-path="url(#face-clip)"/>
    <circle class="white-line" cx="600" cy="474" r="337" fill="none" stroke="var(--white)" stroke-width="2"/>
    <circle class="dot-border" cx="600" cy="474" r="320" fill="none" stroke="var(--gold)" stroke-width="5.5" stroke-linecap="round" stroke-dasharray="0 11.5"/>
    <circle class="brand-mark" cx="600" cy="276" r="68" fill="var(--gold)"/>
  </svg>

  <p class="label__text brand-name">Wabenritter</p>
  <h1 class="label__text product-title">Holzwachs</h1>
  <p class="label__text product-claim">natürliches Holzpflegemittel aus Leinöl &amp; Bienenwachs<br>ohne Lösungsmittel regional von Hand hergestellt</p>
  <p class="label__text net-weight">200 g</p>
  <address class="label__text producer" style="font-style:normal">
    <span class="producer__name">Imkerei Jonas Falkner</span><br>
    Lindenweg 7 • 16818 Wiesenthal<br>
    Tel. +49 160 55501234
  </address>
</main>
</body>
</html>
```